Re-Design Of High Traffic Content Hub

“Tarmac Compass, is a comprehensive online hub dedicated to helping over 150,000 visitors a month have a smooth towing trip. Tarmac Compass is the place where you’ll find up-to-date information, practical advice, ‘how to’ guides and handy tips for your caravan, trailer and anything else you need to tow."

Content on the site is split in to 4 main pillars:
“Caravan” “Trailer” “Boating” "Travel"

Each pillar is split further in to 3 categories:
How To • Products • Reviews

We are crowd-sourcing the redesign of the following pages:

- Home Page
- Category Page
- Single Post
- Search Results
- Static Content Page (Terms & Conditions/ About / Privacy Policy)

Look and feel to be implemented inline with UX best practice.
A strong conversion focus is desirable site wide (e-book downloads & newsletter subscriptions are offered).

Our preference is for the home page to provide the visitor with a visual snapshot of fresh site content and encourage the user to explore the site further using navigation or search.

Design elements to be featured on the home page:
Main Navigation
Site Search
Newsletter Subscription Box
eBook Download CTA
Mission Statement
2 x Recent articles from each top level content pillar including featured image and title.
An area to feature 3 of the site's best performing articles including featured image, title and excerpt.

Mission Statement: "Tarmac Compass is the place you can turn to for up-to-date information, practical advice, ‘how to’ guides and handy tips for your caravan, trailer and anything else worth towing. "

Selected designs will be coded in responsive bootstrap so preference will be given to designs presented with this in mind.

Logo's attached in transparent white and transparent dark.

Live site located at www.tarmaccompass-demo.com.au

ec1f27
f5f5f5
b2b2b2
ffffff

• Strong conversion focus (eBook downloads and newsletter subscriptions)

```html
<!DOCTYPE html>
<html lang="en">
<head>
<meta charset="utf-8">
<title>Tarmac Compass — Home</title>
<link rel="stylesheet" href="https://fonts.googleapis.com/css2?family=Oswald:wght@400;500&family=Open+Sans:wght@400;600&family=Arimo:wght@400;700&display=swap">
<style>
:root{
  --red:#ec1f27;
  --page:#f7f7f7;
  --grey:#b2b2b2;
  --card:#e4e4ea;
  --white:#ffffff;
  --ink:#4a4a4a;
  --dark:#3c3c3c;
  --blue:#3b69c4;
  --social:#8a93a6;
}
*{box-sizing:border-box;margin:0;padding:0}
html,body{width:750px;height:1200px;overflow:hidden;background:var(--page)}
body{position:relative;font-family:"Open Sans",sans-serif;color:var(--ink)}
.abs{position:absolute}

/* header */
.brand{left:76px;top:20px;display:flex;align-items:center;gap:7px;height:20px}
.brand-dot{width:9px;height:9px;border-radius:50%;background:var(--red)}
.brand-name{font-family:"Oswald",sans-serif;font-weight:500;font-size:17px;line-height:20px;color:var(--dark);white-space:nowrap}
.social{display:flex;gap:10px}
.social span{width:15px;height:15px;border-radius:50%;background:var(--social);display:block}
.search{left:457px;top:10px;width:220px;height:22px;background:var(--grey);color:var(--white);font-family:"Oswald",sans-serif;font-size:11px;line-height:22px;padding-left:10px}
.search svg{position:absolute;right:8px;top:6px}
.callout{right:73px;top:40px;text-align:right;font-family:"Oswald",sans-serif;font-size:11px;color:var(--dark);white-space:nowrap}
.callout b{font-weight:500;font-size:16px;color:var(--red);margin-left:8px;vertical-align:-1px}
.nav{left:75px;top:60px;width:600px;height:28px;background:var(--grey)}
.nav a{position:absolute;top:0;line-height:28px;font-family:"Oswald",sans-serif;font-weight:500;font-size:13px;color:var(--white);text-decoration:none}
.nav .home{right:0;width:63px;height:28px;background:var(--red);text-align:center}

/* hero */
.hero{left:0;top:88px;width:750px;height:324px;background:linear-gradient(90deg,#5a3a28 0%,#a45a2e 30%,#c98a4a 55%,#d7a05c 75%,#9a6a3a 100%)}
.hero-photo{position:absolute;inset:0;background:linear-gradient(180deg,rgba(255,240,210,.15) 0%,rgba(0,0,0,0) 55%,rgba(40,25,10,.35) 100%)}
.hero h1{position:absolute;left:389px;top:38px;font-family:"Arimo",sans-serif;font-weight:700;font-size:26px;line-height:32px;color:var(--red)}
.hero p{position:absolute;left:389px;top:112px;font-family:"Arimo",sans-serif;font-weight:700;font-size:11px;color:#7a6a5e}
.hero .more{position:absolute;left:387px;top:148px;width:80px;height:24px;border:1px solid #b9b0a6;font-family:"Arimo",sans-serif;font-size:7.5px;line-height:22px;text-align:center;color:#8d847c}
.dots{position:absolute;left:353px;top:300px;display:flex;gap:6px}
.dots i{width:7px;height:7px;border-radius:50%;background:var(--white);display:block}
.dots i.on{background:var(--red);box-shadow:0 0 0 1.5px var(--white)}

/* tiles */
.tile{position:absolute;overflow:hidden;background:var(--card)}
.tile .img{position:absolute;left:0;top:0;width:100%;height:100%}
.tile.short .img{height:101px}
.tile .tag{position:absolute;left:0;top:6px;background:var(--red);color:var(--white);font-family:"Oswald",sans-serif;font-size:13px;line-height:18px;padding:0 4px}
.tile.wide .tag{top:20px}
.tile p{position:absolute;left:5px;top:109px;right:10px;font-size:6.2px;line-height:8.6px;color:var(--red)}
.g-gauge{background:linear-gradient(135deg,#2a2a2a,#5a5a5a 50%,#3a3a3a)}
.g-wood{background:linear-gradient(135deg,#efe6dc 0%,#cdbfb0 40%,#6e5848 70%,#4a3a30 100%)}
.g-kids{background:linear-gradient(90deg,#a87a4c 0%,#c69a66 30%,#3e2e26 55%,#c89c6a 80%,#a77a4a 100%)}
.g-beach{background:linear-gradient(180deg,#3b8fd6 0%,#7ec0ea 55%,#e8e4d8 75%,#dcd6c6 100%)}

/* side widgets */
.box{position:absolute;background:var(--grey);color:var(--white)}
.box h2{position:absolute;left:9px;top:8px;font-family:"Oswald",sans-serif;font-weight:400;font-size:14.5px;line-height:15px}
.ebook-copy{position:absolute;left:10px;top:44px;width:80px;font-size:5.6px;line-height:7.3px;color:var(--red)}
.ebook-cover{position:absolute;left:97px;top:44px;width:29px;height:38px;background:linear-gradient(160deg,#ffffff 0%,#e7e7e7 30%,#c83a32 50%,#6b6b6b 100%)}
.field{position:absolute;background:var(--white);color:#333;font-size:7px}
.btn{position:absolute;background:var(--red);color:var(--white);font-family:"Arimo",sans-serif;font-weight:700;text-align:center}

.popular{left:526px;top:740px;width:141px}
.popular .img{height:70px;background:linear-gradient(180deg,#3b8fd6 0%,#8cc8ee 70%,#e8e4d8 100%)}
.popular .tag{position:absolute;left:0;top:6px;background:var(--red);color:var(--white);font-family:"Oswald",sans-serif;font-size:13px;line-height:18px;padding:0 4px}
.tabs{display:flex;height:20px;font-size:7px;line-height:20px;text-align:center}
.tabs span{flex:1;background:var(--white);color:var(--blue)}
.tabs span.on{background:var(--blue);color:var(--white)}
.post{position:absolute;left:526px;width:141px;height:45px;background:var(--card)}
.post .thumb{position:absolute;left:1px;top:1px;width:46px;height:43px}
.post span{position:absolute;left:56px;top:7px;right:4px;font-size:7px;line-height:9.5px;color:#333}

/* mission */
.mission h3{font-family:"Oswald",sans-serif;font-weight:500;font-size:12px;color:var(--red)}
.mission p{margin-top:5px;font-size:8.6px;line-height:13px;color:#555}

/* footer */
.footer{left:0;top:1092px;width:750px;height:108px;background:var(--red);color:var(--white);text-align:center}
.footer .social{position:absolute;left:329px;top:14px;gap:11px}
.footer .social span{background:#c9cfe0}
.footer nav{position:absolute;left:0;right:0;top:40px;font-family:"Oswald",sans-serif;font-weight:500;font-size:13px}
.footer nav a{color:var(--white);text-decoration:none;margin:0 10px}
.footer small{position:absolute;left:0;right:0;top:66px;font-family:"Arimo",sans-serif;font-weight:700;font-size:6.5px}
</style>
</head>
<body>

<header>
  <div class="abs brand" aria-label="Tarmac Compass">
    <span class="brand-dot"></span>
    <span class="brand-name">TARMAC COMPASS</span>
  </div>
  <div class="abs social" style="left:355px;top:14px" aria-label="Social links"><span></span><span></span><span></span><span></span></div>
  <div class="abs search">SEARCH
    <svg width="10" height="10" viewBox="0 0 10 10"><circle cx="4" cy="4" r="3" fill="none" stroke="#fff" stroke-width="1.3"/><path d="M6.2 6.2 9 9" stroke="#fff" stroke-width="1.4"/></svg>
  </div>
  <div class="abs callout">CALL NOW TO SCHEDULE A FREE CONSULTATION <b>+44 219-000-0199</b></div>
  <nav class="abs nav">
    <a style="left:16px">CARAVAN</a>
    <a style="left:86px">TRAILERS</a>
    <a style="left:156px">BOATS</a>
    <a style="left:211px">TRAVEL</a>
    <a class="home">HOME</a>
  </nav>
</header>

<section class="abs hero">
  <div class="hero-photo" role="img" aria-label="Photo of a man resting against a vehicle at sunset in an open field"></div>
  <h1>5 Tips For Hitching<br>Up Your Caravan</h1>
  <p>Our top five tips to make hitching your caravan a breeze</p>
  <div class="more">VIEW MORE</div>
  <div class="dots"><i></i><i class="on"></i><i></i><i></i></div>
</section>

<main>
  <article class="tile short" style="left:86px;top:420px;width:141px;height:140px">
    <div class="img g-gauge" role="img" aria-label="Photo of a tyre pressure gauge"></div>
    <span class="tag">CARAVANING</span>
    <p>Here's how to establish and maintain the correct pressures for your caravan's tyres.</p>
  </article>
  <article class="tile wide" style="left:233px;top:420px;width:288px;height:140px">
    <div class="img g-wood" role="img" aria-label="Photo of hands holding a trailer jack handle on a wooden deck"></div>
    <span class="tag">TRAILERS</span>
  </article>

  <article class="tile wide" style="left:87px;top:566px;width:289px;height:140px">
    <div class="img g-kids" role="img" aria-label="Photo of two children peeking out of a caravan bunk"></div>
    <span class="tag">TRAVEL</span>
  </article>
  <article class="tile short" style="left:380px;top:566px;width:141px;height:140px">
    <div class="img g-gauge" role="img" aria-label="Photo of a tyre pressure gauge"></div>
    <span class="tag">BOATING</span>
    <p>Here's how to establish and maintain the correct pressures for your caravan's tyres.</p>
  </article>

  <article class="tile short" style="left:87px;top:714px;width:141px;height:140px">
    <div class="img g-beach" role="img" aria-label="Photo of a boat trailer on a beach"></div>
    <span class="tag">BOATING</span>
    <p>Here's how to establish and maintain the correct pressures for your caravan's tyres.</p>
  </article>
  <article class="tile wide" style="left:233px;top:714px;width:288px;height:140px">
    <div class="img g-kids" role="img" aria-label="Photo of two children peeking out of a caravan bunk"></div>
    <span class="tag">TRAVEL</span>
  </article>

  <article class="tile wide" style="left:87px;top:862px;width:288px;height:140px">
    <div class="img g-wood" role="img" aria-label="Photo of hands holding a trailer jack handle on a wooden deck"></div>
    <span class="tag">TRAILERS</span>
  </article>
  <article class="tile short" style="left:380px;top:862px;width:141px;height:140px">
    <div class="img g-gauge" role="img" aria-label="Photo of a tyre pressure gauge"></div>
    <span class="tag">BOATING</span>
    <p>Here's how to establish and maintain the correct pressures for your caravan's tyres.</p>
  </article>

  <section class="abs mission" style="left:90px;top:1022px;width:425px">
    <h3>Mission Statement</h3>
    <p>Tarmac Compass is the place you can turn to for up-to-date information, practical advice, ‘how to’ guides and handy tips for your caravan, trailer and anything else worth towing</p>
  </section>
</main>

<aside>
  <div class="box" style="left:526px;top:420px;width:140px;height:140px">
    <h2>DOWNLOAD OUR<br>FREE E-BOOK</h2>
    <div class="ebook-copy">Our towing e-book, packed full of essential safety, preparation and towing tips will be the perfect driving companion. Receive your free e-book and sign up to our</div>
    <div class="ebook-cover" role="img" aria-label="E-book cover"></div>
    <div class="field" style="left:8px;top:90px;width:126px;height:18px;line-height:18px;text-align:center">Enter Your Email Address</div>
    <div class="btn" style="left:8px;top:115px;width:126px;height:19px;line-height:19px;font-size:8.5px">DOWNLOAD
      <svg style="position:absolute;right:9px;top:4px" width="11" height="11" viewBox="0 0 11 11"><circle cx="5.5" cy="5.5" r="5.5" fill="#fff"/><path d="M3 4.5 5.5 7 8 4.5" fill="none" stroke="#ec1f27" stroke-width="1.5"/></svg>
    </div>
  </div>

  <div class="box" style="left:526px;top:566px;width:140px;height:140px">
    <h2>SUBSCRIBE TO<br>OUR NEWSLETTER</h2>
    <div class="field" style="left:9px;top:84px;width:123px;height:19px;line-height:19px;padding-left:8px">Enter your email address</div>
    <div class="btn" style="left:9px;top:111px;width:63px;height:19px;line-height:19px;font-size:7px;font-family:'Open Sans',sans-serif;font-weight:600">SUBSCRIBE</div>
    <svg style="position:absolute;left:76px;top:114px" width="11" height="9" viewBox="0 0 11 9"><rect x=".5" y=".5" width="10" height="8" fill="#fff" stroke="#999"/><path d="M.5 .5 5.5 5 10.5 .5" fill="none" stroke="#999"/></svg>
  </div>

  <div class="abs popular">
    <div class="img" role="img" aria-label="Photo of a boat trailer on a beach"></div>
    <span class="tag">BOATING</span>
    <div class="tabs"><span>POPULAR</span><span class="on">RECENT</span></div>
  </div>
  <div class="post" style="top:836px"><div class="thumb" style="background:linear-gradient(135deg,#f2f2f2,#c8d2c8)" role="img" aria-label="Phone showing a tracking map"></div><span>How To Theft-Proof Your Caravan</span></div>
  <div class="post" style="top:888px"><div class="thumb" style="background:linear-gradient(135deg,#3a3a3a,#8a8a8a)" role="img" aria-label="Suspension coil springs"></div><span>New Caravan Suspension Launched</span></div>
  <div class="post" style="top:940px"><div class="thumb" style="background:linear-gradient(135deg,#6a4a3a,#c42a2a)" role="img" aria-label="Portable red generator"></div><span>How To Use A Generator</span></div>
  <div class="post" style="top:994px"><div class="thumb" style="background:linear-gradient(135deg,#d8d4cc,#8a8478)" role="img" aria-label="Campsite by the coast"></div><span>Top 3 North Queensland Campsites</span></div>
</aside>

<footer class="abs footer">
  <div class="social" aria-label="Social links"><span></span><span></span><span></span><span></span></div>
  <nav><a>CARAVAN</a><a>TRAILERS</a><a>BOATS</a><a>TRAVEL</a></nav>
  <small>© 2016 ALL RIGHT RESERVED WWW.TARMACCOMPASS-DEMO.COM.AU</small>
</footer>

</body>
</html>
```